Web Design for Webdesign company 3 page PSD

Project
---------
We need a PSD Web Design to be used in a WordPress installation.
What we would like to create is a professional looking website for a web design agency. We also need you to look for suitable stock images to be placed on these pages.
We need the design for:
Homepage
Landing page
Contact page
attached in the pages file you will find a file with more in depth details how these files should be build up.
We would like to see a desktop version and a mobile version of these pages
The website should have a 1100px width.
The mobile design should have 480px width.
The homepage should have a header slider about 450px high.
The slider is preferred full width and should have some images text and a button
Objectives
-------------
The main objective for the website is to get leads from customers in the form of a request for a quotation or a call or mail me back action. The most important action for the homepage is to link and navigate to our landing pages.
What we want to tell our visitors (our main products)
-------------------------------------------------------------------
- A website with no big investment but a monthly rate
- A successful website with no worries (a complete website, seo, hosting and a service contract for future customization is included for a monthly rate)
Color Scheme
------------
Use branding colors. You can find them in the branding.pdf file.
Additional colors:
White: #ffffff
Black: #181818
Company info
--------------
We are a starting web design / marketing agency based in The Netherlands and looking for the design of our website. Our services are (custom) webdesign, website marketing or combinations of both. Our main customer group is small business owners.
We sell websites but give the option to buy it with a lease contract.
A second product is a default website with a complete service: SEO, hosting and a service contract for a monthly rate.
Content:
-----------
If not available place Lorem Ipsum text.
There will come about 400 words of text on the landing pages
Design Competition
--------------------------
Since this is a designing competition we would like to see your creativity.
What you can expect from us is a lot of feedback 7 days a week with short response time.
You can send us the first sketchy mock ups of the homepage and we will give feedback based on these design. But we like your feedback or comments as well
Read the pages file for more in depth details how the pages should be designed

Target Market(s)
Small business owners in The Netherlands
Industry/Entity Type
It Company
Number of Pages Required
3 page
Requirements
Must have
- Homepage:
- Header slider with images, some text and a link to a custom page
- The slider should have 3 designed slides
- Landings page:
- Sidebar
- Action button for a request for a quotation
- Action button for a call me back action
- Action button for an appointment
- Contact form:
- Address details
- Contact form
Nice to have
- Homepage:
- Full width slider
- Testimonial block
- Blog items
Should not have
- Flash
- A to crowded design

```html
<!DOCTYPE html>
<html lang="en">
<head>
<meta charset="utf-8">
<title>Oakline Web Studio — Responsive Web Design</title>
<link rel="stylesheet" href="https://fonts.googleapis.com/css2?family=Raleway:wght@400;500;600&family=Open+Sans:ital,wght@0,400;0,600;1,400&display=swap">
<style>
:root{
  --white:#ffffff;
  --black:#0b0b0b;
  --ink:#222222;
  --muted:#777777;
  --teal-dark:#2c5c60;
  --teal:#2f6d76;
  --teal-light:#3b8a90;
  --green:#5a8c72;
  --grey-bg:#f2f2f2;
  --line:#e2e2e2;
  --bar:#2a2a2a;
}
*{box-sizing:border-box;margin:0;padding:0}
html,body{width:1200px;height:2169px;overflow:hidden}
body{font-family:"Open Sans",Arial,sans-serif;color:var(--ink);background:var(--white);position:relative}
h1,h2,h3,h4,.nav a,.brand{font-family:"Raleway",Arial,sans-serif}

/* header */
.site-header{height:97px;border-bottom:1px solid var(--line);position:relative}
.brand{position:absolute;left:210px;top:30px;display:flex;align-items:center;gap:10px;font-weight:600;font-size:21px;color:var(--teal-dark);line-height:1}
.brand .mark{width:26px;height:26px;border-radius:50%;background:var(--green)}
.nav{position:absolute;left:585px;top:44px;display:flex}
.nav a{font-size:12.5px;text-decoration:none;color:#777;letter-spacing:.3px;margin-right:40px;position:relative;padding-bottom:10px}
.nav a.active{color:var(--teal)}
.nav a.active::after{content:"";position:absolute;left:0;right:0;bottom:0;height:2px;background:var(--teal)}

/* hero */
.hero{position:relative;height:493px;background:linear-gradient(90deg,#b9b9b9,#dcdcdc 35%,#d6d6d6 65%,#a9a9a9);overflow:hidden}
.hero-photo{position:absolute;inset:0}
.hero-title{position:absolute;top:45px;width:100%;text-align:center;font-family:"Raleway",sans-serif;font-weight:500;font-size:44px;letter-spacing:3px;color:var(--teal-dark)}
.hero-sub{position:absolute;top:94px;width:100%;text-align:center;font-family:"Raleway",sans-serif;font-weight:500;font-size:18px;letter-spacing:2px;color:#2b3f40}
.btn{display:inline-block;font-family:"Raleway",sans-serif;font-size:12px;color:var(--white);text-decoration:none;text-align:center;letter-spacing:.3px}
.btn-cta{position:absolute;left:542px;top:132px;width:120px;height:30px;line-height:30px;background:var(--teal)}
.hero-devices{position:absolute;left:320px;top:186px;width:542px;height:272px;background:linear-gradient(180deg,#4a4e54,#2a2d31);border-radius:6px}
.hero-arrow{position:absolute;top:198px}
.hero-arrow.prev{left:170px}
.hero-arrow.next{left:990px}

/* services */
.services{height:293px;position:relative}
.service{position:absolute;top:42px;width:200px;text-align:center}
.service .hex{display:block;margin:0 auto}
.service h3{font-weight:400;font-size:17.5px;color:#222;margin-top:10px}
.service p{font-size:9.5px;line-height:13px;color:var(--muted);margin:8px auto 0;width:190px}
.service .btn{background:var(--green);width:87px;height:27px;line-height:27px;margin-top:14px;font-size:11px}

/* about */
.about{background:var(--black);height:350px;position:relative;color:var(--white)}
.about h2{position:absolute;left:210px;top:75px;font-weight:400;font-size:26px}
.about .copy{position:absolute;left:210px;top:116px;width:395px;font-size:9.5px;line-height:14.5px}
.about .copy p+p{margin-top:12px}
.about .btn{position:absolute;left:210px;top:232px;width:130px;height:33px;line-height:33px;background:var(--green);font-size:12px}
.about-photo{position:absolute;left:646px;top:66px;width:343px;height:215px;background:linear-gradient(135deg,#8c9aa6,#d8d6cf 55%,#6e665a)}

/* projects & blog */
.feeds{height:355px;position:relative}
.feeds h2{position:absolute;top:44px;font-weight:400;font-size:23px}
.feeds .projects-title{left:210px;color:var(--teal-light)}
.feeds .blog-title{left:652px;color:#222}
.project{position:absolute;left:210px;width:390px;height:82px}
.project .thumb{position:absolute;left:0;top:0;width:128px;height:82px;background:linear-gradient(135deg,#2a2a2a,#5a5f66)}
.project h4,.post h4{font-weight:400;font-size:12.5px;color:#333}
.project h4{position:absolute;left:138px;top:0}
.project p{position:absolute;left:138px;top:22px;width:252px;font-size:9px;line-height:14.5px;color:var(--muted)}
.blog-list{position:absolute;left:652px;top:88px;width:340px}
.post+.post{margin-top:12px}
.post p{font-size:8.5px;line-height:13.5px;color:var(--muted);margin-top:5px}
.post a{display:block;font-size:10px;color:var(--teal-dark);text-decoration:none;margin-top:5px;font-weight:600}

/* testimonials */
.testimonials{background:var(--grey-bg);height:320px;position:relative;border-top:1px solid var(--line)}
.testimonials h2{position:absolute;top:40px;width:100%;text-align:center;font-weight:400;font-size:24px;letter-spacing:.5px;color:#222}
.quote{position:absolute;top:87px;width:252px;height:133px;background:var(--white);border:1px solid #ddd}
.quote p{font-style:italic;font-size:9.5px;line-height:16px;color:#555;text-align:center;padding:13px 14px 0}
.quote .avatar{position:absolute;left:98px;top:98px;width:56px;height:56px;border-radius:50%;border:3px solid var(--white);background:linear-gradient(135deg,#c9a48a,#e7d3c3)}
.quote cite{position:absolute;top:162px;width:100%;text-align:center;font-style:normal;font-size:10px;color:#444}

/* footer */
.site-footer{background:var(--black);height:212px;position:relative;color:var(--white)}
.site-footer h4{font-weight:500;font-size:13.5px;letter-spacing:.3px}
.fcol{position:absolute;top:47px}
.fcol ul{list-style:none;margin-top:8px}
.fcol li{font-size:9.5px;line-height:20px}
.fcol p{font-size:9.5px;line-height:20px}
.newsletter input{display:block;width:184px;height:26px;margin-top:10px;border:0;padding:0 10px;font-size:9px;font-family:"Open Sans",sans-serif}
.newsletter .btn{width:92px;height:27px;line-height:27px;background:var(--green);margin-top:11px;font-size:11px}
.socials{display:flex;gap:10px;margin-top:10px}
.socials span{width:14px;height:14px;border-radius:50%;background:var(--white)}
.footer-brand{position:absolute;left:828px;top:85px;display:flex;align-items:center;gap:8px;font-family:"Raleway",sans-serif;font-weight:600;font-size:17px;color:var(--green)}
.footer-brand .mark{width:22px;height:22px;border-radius:50%;background:var(--green)}
.legal{position:absolute;left:0;top:2122px;width:1200px;height:47px;background:var(--bar);color:#bbb;font-size:9.5px}
.legal p{position:absolute;left:215px;top:16px}
</style>
</head>
<body>

<header class="site-header">
  <div class="brand"><span class="mark"></span>Oakline Web Studio</div>
  <nav class="nav">
    <a class="active" href="#">HOME</a>
    <a href="#">ABOUT US</a>
    <a href="#">SERVICES</a>
    <a href="#">PROJECTS</a>
    <a href="#">CONTACT</a>
  </nav>
</header>

<section class="hero">
  <div class="hero-photo" role="img" aria-label="Black and white photo of a team working together in an office"></div>
  <h1 class="hero-title">RESPONSIVE WEB DESIGN</h1>
  <p class="hero-sub">YOUR WEBSITE READABLE ON ALL DEVICES</p>
  <a class="btn btn-cta" href="#">CALL TO ACTION</a>
  <div class="hero-devices" role="img" aria-label="Website shown on desktop, laptop, tablet and phone screens"></div>
  <svg class="hero-arrow prev" width="30" height="70" viewBox="0 0 30 70"><polyline points="26,2 4,35 26,68" fill="none" stroke="#fff" stroke-width="2"/></svg>
  <svg class="hero-arrow next" width="30" height="70" viewBox="0 0 30 70"><polyline points="4,2 26,35 4,68" fill="none" stroke="#fff" stroke-width="2"/></svg>
</section>

<section class="services">
  <div class="service" style="left:253px">
    <svg class="hex" width="90" height="96" viewBox="0 0 90 96"><polygon points="45,0 90,24 90,72 45,96 0,72 0,24" fill="#5a8c72"/><rect x="31" y="39" width="28" height="20" rx="2" fill="#fff"/><rect x="39" y="34" width="12" height="6" rx="1" fill="none" stroke="#fff" stroke-width="2.5"/><rect x="31" y="47" width="28" height="2" fill="#5a8c72"/></svg>
    <h3>Web Development</h3>
    <p>acilisis massa Etiam eu urna Sed porta Suspendisse quam leo molestie sed luctus quis feugiat in pede Fusce tellus</p>
    <a class="btn" href="#">CLICK HERE</a>
  </div>
  <div class="service" style="left:493px">
    <svg class="hex" width="90" height="96" viewBox="0 0 90 96"><polygon points="45,0 90,24 90,72 45,96 0,72 0,24" fill="#5a8c72"/><circle cx="45" cy="40" r="6" fill="#fff"/><circle cx="33" cy="43" r="4.5" fill="#fff"/><circle cx="57" cy="43" r="4.5" fill="#fff"/><path d="M35 60a10 10 0 0 1 20 0z" fill="#fff"/><path d="M25 60a8 8 0 0 1 14-5v5z" fill="#fff"/><path d="M65 60a8 8 0 0 0-14-5v5z" fill="#fff"/></svg>
    <h3>Web Designing</h3>
    <p>acilisis massa Etiam eu urna Sed porta Suspendisse quam leo molestie sed luctus quis feugiat in pede Fusce tellus</p>
    <a class="btn" href="#">CLICK HERE</a>
  </div>
  <div class="service" style="left:735px">
    <svg class="hex" width="90" height="96" viewBox="0 0 90 96"><polygon points="45,0 90,24 90,72 45,96 0,72 0,24" fill="#5a8c72"/><circle cx="45" cy="48" r="10" fill="none" stroke="#fff" stroke-width="7" stroke-dasharray="5 2.85"/><circle cx="45" cy="48" r="9" fill="#fff"/><circle cx="45" cy="48" r="4" fill="#5a8c72"/></svg>
    <h3>Programming &amp; SEO</h3>
    <p>acilisis massa Etiam eu urna Sed porta Suspendisse quam leo molestie sed luctus quis feugiat in pede Fusce tellus</p>
    <a class="btn" href="#">CLICK HERE</a>
  </div>
</section>

<section class="about">
  <h2>ABOUT OUR COMPANY</h2>
  <div class="copy">
    <p>Curabitur iaculis tempus eros Curabitur vel mi sit amet magna malesuada ultrices Ut nisi erat fermentum vel congue id euismod in elit Fusce ultricies orci</p>
    <p>Morbi ornare gravida elit Integer congue augue et malesuada iaculis ipsum dui aliquet felis at cursus magna nisl nec elit Praesent elementum elit at tellus nec ultricies sit amet porttitor mattis enim In massa libero interdum nec interdum vel blandit sed nulla In ullamcorper est eget tempor cursus</p>
  </div>
  <a class="btn" href="#">CALL TO ACTION</a>
  <div class="about-photo" role="img" aria-label="Photo of colleagues working at desks with laptops"></div>
</section>

<section class="feeds">
  <h2 class="projects-title">Latest Projects</h2>
  <h2 class="blog-title">Latest Blog</h2>
  <article class="project" style="top:91px">
    <div class="thumb" role="img" aria-label="Screenshot of a dark website project"></div>
    <h4>Ut nisi erat fermentum</h4>
    <p>Donec quis mi sed magna hendrerit accumsan Suspendisse risus nibh ultricies eu volutpat non condimentum hendrerit augue Etiam eleifend metus vitae adipiscing semper mauris ipsum iaculis elit congue gravida elit mi egestas orci</p>
  </article>
  <article class="project" style="top:204px">
    <div class="thumb" role="img" aria-label="Screenshot of a business website project"></div>
    <h4>Nunc porta convallis pede</h4>
    <p>Donec quis mi sed magna hendrerit accumsan Suspendisse risus nibh ultricies eu volutpat non condimentum hendrerit augue Etiam eleifend metus vitae adipiscing semper mauris ipsum iaculis elit congue gravida elit mi egestas orci</p>
  </article>
  <div class="blog-list">
    <article class="post">
      <h4>Praesent sit amet est In dictum</h4>
      <p>Vivamus porttitor purus nisi eleifend libero a tempus libero lectus feugiat felis Morbi diam mauris viverra</p>
      <a href="#">Read More</a>
    </article>
    <article class="post">
      <h4>Nunc porta convallis pede</h4>
      <p>Donec quis mi sed magna hendrerit accumsan Suspendisse risus nibh ultricies eu</p>
      <a href="#">Read More</a>
    </article>
    <article class="post">
      <h4>Mauris vel lacus vitae felis</h4>
      <p>volutpat non condimentum hendrerit augue Etiam eleifend metus vitae adipiscing semper mauris ipsum iaculis elit congue gravida elit</p>
      <a href="#">Read More</a>
    </article>
  </div>
</section>

<section class="testimonials">
  <h2>TESTIMONIALS</h2>
  <blockquote class="quote" style="left:205px">
    <p>Morbi diam mauris viverra in gravida eu mattis in ante Morbi eget arcu Morbi porta libero id ullam-corper nonummy nibh ligula pulvinar metus eget consectetuer augue nisi quis lacus Ut ac</p>
    <div class="avatar" role="img" aria-label="Portrait of the client"></div>
    <cite>By Author Name, City Location</cite>
  </blockquote>
  <blockquote class="quote" style="left:468px">
    <p>Morbi diam mauris viverra in gravida eu mattis in ante Morbi eget arcu Morbi porta libero id ullam-corper nonummy nibh ligula pulvinar metus eget consectetuer augue nisi quis lacus Ut ac</p>
    <div class="avatar" role="img" aria-label="Portrait of the client"></div>
    <cite>By Author Name, City Location</cite>
  </blockquote>
  <blockquote class="quote" style="left:731px">
    <p>Morbi diam mauris viverra in gravida eu mattis in ante Morbi eget arcu Morbi porta libero id ullam-corper nonummy nibh ligula pulvinar metus eget consectetuer augue nisi quis lacus Ut ac</p>
    <div class="avatar" role="img" aria-label="Portrait of the client"></div>
    <cite>By Author Name, City Location</cite>
  </blockquote>
</section>

<footer class="site-footer">
  <div class="fcol" style="left:217px">
    <h4>COMPANY</h4>
    <ul><li>About Us</li><li>Why Choose Us</li><li>Our Team</li><li>Testimonials</li><li>Blogs</li></ul>
  </div>
  <div class="fcol newsletter" style="left:366px">
    <h4>NEWSLETTER SIGN UP</h4>
    <p>Please sign up here for latest deals</p>
    <input type="email" placeholder="Email address">
    <a class="btn" href="#">SUBSCRIBE</a>
  </div>
  <div class="fcol" style="left:623px;top:42px">
    <h4>CONTACT US</h4>
    <p style="margin-top:4px">Oakline Web Studio Ltd</p>
    <p>24 Maple Lane, Suite 3, Riverton 40210</p>
    <p>Phone: 555.014.2278</p>
    <p>Email: hello@oaklinestudio.example</p>
    <div class="socials"><span></span><span></span><span></span><span></span></div>
  </div>
  <div class="footer-brand"><span class="mark"></span>Oakline Web Studio</div>
</footer>

<div class="legal"><p>© 2015 Company Name &nbsp;All right reserved &nbsp;Term of Use</p></div>

</body>
</html>
```